HTML Web Design for RivoLink Website

I require a non functioning web design in HTML format.
The website is for an online platform for connecting contract geoscientists with employers looking for short term geologists and geophysicists.
There will be 12 pages plus 3 sub pages of design to complete in total, but for your submission, please provide three pages and one sub page for review. These are to be submitted upon you winning the design contest, and then you can complete the rest of the pages in the days following that.
Please provide your designs for the Home Page, Contractor Profile Page and the Search Page / Search Results List.
Please review my design brief, and mockup of some of the pages carefully. Also, please find attached my logo.
Note, my logo is red, but I do not want a red dominated design, please use red as an accent colour.

Target Market(s)

Geoscientists

Industry/Entity Type

Oil And Gas

Number of Pages Required

5+ page

Requirements
Must have
• HTML format designs
• Submit 3 pages for competition, but further pages after winner is selected
• Professional and modern
Nice to have
• Some red accent
Should not have
• Too much red

```html
<!DOCTYPE html>
<html lang="en">
<head>
<meta charset="utf-8">
<title>RivoLink – Contract Geoscientists Worldwide</title>
<link href="https://fonts.googleapis.com/css2?family=Montserrat:wght@400;600;700&family=Open+Sans:ital,wght@0,400;0,600;0,700;1,400&display=swap" rel="stylesheet">
<style>
:root{
  --red:#e8435a;
  --red-deep:#c9344a;
  --ink:#222;
  --dark:#1d1d1d;
  --slate-1:#2a2c31;
  --slate-2:#3b3e45;
  --slate-3:#33363c;
  --grey:#e5e5e5;
  --white:#fff;
  --muted:#555;
}
*{box-sizing:border-box;margin:0;padding:0}
html,body{width:1200px;height:2590px;overflow:hidden}
body{position:relative;font-family:"Open Sans",sans-serif;color:var(--ink);background:var(--white)}
.section{position:absolute;left:0;width:1200px;overflow:hidden}
.abs{position:absolute}
.center{text-align:center;left:0;width:1200px}

/* hero */
.hero{top:0;height:480px}
.hero-photo{position:absolute;inset:0;background:radial-gradient(ellipse at 50% 45%,#5a5a5e 0%,#3a3b40 40%,#1b1c20 100%)}
.nav{position:absolute;top:0;left:0;width:1200px;height:66px}
.brand{position:absolute;top:14px;left:250px;font-family:"Montserrat",sans-serif;font-weight:700;font-size:26px;color:var(--white);letter-spacing:.5px;display:flex;align-items:center;gap:8px}
.brand-dot{width:12px;height:12px;background:var(--white)}
.nav-links{position:absolute;top:26px;left:454px;display:flex;gap:17px;list-style:none;font-family:"Montserrat",sans-serif;font-size:10px;color:#e9e9e9;text-transform:uppercase}
.nav-links .active{font-weight:700;color:var(--white)}
.hero-title{top:172px;font-family:"Montserrat",sans-serif;font-weight:700;font-size:31px;color:var(--white)}
.hero-sub{top:214px;left:290px;width:620px;font-size:17.5px;line-height:21px;color:#eee;text-align:center}
.btn{position:absolute;display:flex;align-items:center;justify-content:center;font-family:"Montserrat",sans-serif;font-weight:600;font-size:11px}
.btn-red{background:var(--red);color:var(--white)}
.btn-white{background:var(--white);color:var(--ink)}
.btn-dark{background:#3a3a3a;color:var(--white)}
.scroll-down{position:absolute;left:584px;top:426px}

/* how it works */
.how{top:480px;height:280px;background:var(--grey)}
.stripe-band{position:absolute;left:0;top:0;width:1200px;height:62px;background:repeating-linear-gradient(135deg,#e9e9e9 0 6px,#e2e2e2 6px 8px)}
.title{font-family:"Montserrat",sans-serif;font-weight:700;font-size:26px;color:var(--ink)}
.title .accent{color:var(--red)}
.title-light{font-family:"Open Sans",sans-serif;font-weight:400;font-size:24px;color:var(--ink)}
.title-light .accent{color:var(--red)}
.title-light b{font-weight:700}
.how-title{top:14px}
.how-copy{top:72px;left:275px;width:650px;font-size:12.5px;line-height:18px;color:var(--muted);text-align:center}
.how-copy b{color:var(--ink)}
.how-copy p+p{margin-top:14px}

/* neutral photo bands */
.band-photo{position:absolute;left:0;width:1200px;background:linear-gradient(90deg,var(--slate-1) 0%,var(--slate-2) 50%,var(--slate-1) 100%)}
.band-photo.alt{background:linear-gradient(90deg,#26282d 0%,var(--slate-3) 50%,#26282d 100%)}
.ribbon{position:absolute;left:0;top:0}

.signin{top:760px;height:262px}
.signin-title{top:8px}
.field{position:absolute;height:20px;border:1px solid rgba(255,255,255,.55);color:var(--white);font-size:9px;padding:0 8px;display:flex;align-items:center;justify-content:space-between}
.chev{width:9px;height:6px}
.captcha{position:absolute;background:var(--white);display:flex;align-items:center;gap:8px;padding-left:6px;font-size:9px;color:#444}
.captcha .box{width:14px;height:14px;border:1px solid #aaa;background:var(--white)}
.captcha .badge{margin-left:auto;margin-right:10px;width:18px;height:18px;background:#8aa4c8}
.form-btn{position:absolute;background:var(--red);color:var(--white);font-family:"Montserrat",sans-serif;font-weight:600;font-size:10.5px;letter-spacing:1.5px;display:flex;align-items:center;justify-content:center}

/* employer search */
.search{top:1022px;height:425px;background:var(--grey)}
.search-title{top:14px}
.panel-head{position:absolute;height:31px;background:var(--red);color:var(--white);font-family:"Open Sans",sans-serif;font-size:13px;letter-spacing:.8px;display:flex;align-items:center;justify-content:center}
.filter{position:absolute;left:264px;width:328px;height:26px;background:var(--white);border:1px solid #cfcfcf;font-size:9px;color:#555;padding:0 8px;display:flex;align-items:center}
.filter .value{margin-left:auto;margin-right:8px;color:#333}
.search-btn{position:absolute;left:264px;top:345px;width:328px;height:32px;background:var(--red);color:var(--white);font-size:10.5px;font-weight:700;letter-spacing:1.4px;display:flex;align-items:center;justify-content:center}
.result-panel{position:absolute;left:609px;top:148px;width:328px;height:254px;background:#f4f4f4}

/* testimonials */
.testimonial{top:1447px;height:254px}
.quote{top:60px;left:255px;width:690px;font-style:italic;font-size:12.5px;line-height:17px;color:var(--white);text-align:center}
.quote-mark{top:119px;font-size:14px;font-weight:700;color:var(--red)}
.avatar{position:absolute;left:571px;top:133px;width:58px;height:58px;border-radius:50%;border:2px solid var(--white);background:linear-gradient(#6b5f58,#3b3533)}
.person{top:198px;font-size:9px;font-weight:700;color:var(--white)}
.role{top:212px;font-size:7.5px;color:var(--red);letter-spacing:.3px}
.dots{position:absolute;top:228px;left:585px;display:flex;gap:4px}
.dots span{width:7px;height:7px;border-radius:50%;border:1px solid var(--white)}
.dots span.on{background:var(--white)}

/* team */
.team{top:1701px;height:323px;background:linear-gradient(90deg,#1a1a1a,#262626 50%,#1a1a1a)}
.team-title{top:10px;font-family:"Open Sans",sans-serif;font-weight:700;font-size:25px;color:var(--white);letter-spacing:1.2px}
.card{position:absolute;top:60px;width:162px;height:200px}
.card-photo{width:162px;height:161px;background:linear-gradient(160deg,#cfd6dc,#8f9aa3)}
.card-caption{height:39px;background:#d4d4d4;text-align:center;padding-top:7px}
.card-name{font-size:8.5px;font-weight:700;color:#333;letter-spacing:.3px}
.card-role{font-size:8px;color:var(--red)}
.ghost-btn{position:absolute;left:540px;top:279px;width:120px;height:25px;border:1.5px solid var(--white);border-radius:13px;color:var(--white);font-size:7.5px;font-weight:700;letter-spacing:.8px;display:flex;align-items:center;justify-content:center}

/* contact */
.contact{top:2024px;height:276px}
.contact-title{top:6px}

/* footer */
.footer{top:2300px;height:290px;background:radial-gradient(ellipse at 50% 40%,#3a3a3a,#1a1a1a 70%)}
.footer-brand{top:36px;font-family:"Montserrat",sans-serif;font-weight:700;font-size:44px;color:var(--white);display:flex;justify-content:center;align-items:center;gap:12px}
.footer-brand .brand-dot{width:16px;height:16px}
.footer-info{top:131px;font-size:11.5px;line-height:15px;color:var(--white);letter-spacing:.4px}
.footer-info b{font-weight:700}
.footer-info .sep{color:var(--red);margin:0 8px}
.social{position:absolute;left:528px;top:179px;width:142px;height:27px;border-radius:14px;background:var(--red);display:flex;align-items:center;justify-content:center;gap:13px}
.social span{width:9px;height:9px;border-radius:50%;background:var(--white)}
.copyright{top:229px;font-size:10.5px;color:var(--white);letter-spacing:.8px}
.copyright a{color:var(--white);text-decoration:underline}
</style>
</head>
<body>

<header class="section hero">
  <div class="hero-photo" role="img" aria-label="Photo of smiling business people in suits at a meeting, darkened"></div>
  <nav class="nav">
    <div class="brand"><span class="brand-dot"></span>RivoLink</div>
    <ul class="nav-links">
      <li>Home</li><li>How it works</li><li>Registration</li><li>Contractor Profile</li><li>Search</li><li>Testimonials</li><li class="active">Contact us</li>
    </ul>
  </nav>
  <h1 class="abs center hero-title">Contract Geoscientists Worldwide</h1>
  <p class="abs hero-sub">RivoLink is an online platform for matching mining and oil and gas industry employers with short term needs to registered geoscience consultants.</p>
  <a class="btn btn-red" style="left:456px;top:280px;width:140px;height:36px">Join Free Today</a>
  <a class="btn btn-white" style="left:604px;top:280px;width:139px;height:36px">Register Now</a>
  <svg class="scroll-down" width="32" height="32" viewBox="0 0 32 32" aria-hidden="true">
    <circle cx="16" cy="16" r="14" fill="none" stroke="#fff" stroke-width="1.5"/>
    <path d="M10 13l6 6 6-6" fill="none" stroke="#fff" stroke-width="1.8"/>
  </svg>
</header>

<section class="section how">
  <div class="stripe-band"></div>
  <h2 class="abs center title how-title">RivoLink <span class="accent">How It</span> Works</h2>
  <div class="abs how-copy">
    <p><b>RivoLink is an online platform that connects businesses with a global network of top</b> independent consultants for project based work Lorem ipsum dolor sitmetconsectetur adipiscing elitliquam sagittis massavs egetnuncinia egegnissim etfelisunc nec ex lacinia metus sodales</p>
    <p><b>To enable businesses of all sizes to directly engage top consulting talent for project based work.</b> talipsumtaCurabitur arcu neque, lacinia eget dignir project based work Lorem ipsum dolor sitmetconsectetur adipiscing elitliquam sagittis massavs egetnuncinia egegnissim etfelisunc nesslaciurabiturarcuned.</p>
  </div>
  <a class="btn btn-red" style="left:485px;top:217px;width:99px;height:32px;font-size:10px">Contractor Sign in</a>
  <a class="btn btn-dark" style="left:590px;top:217px;width:123px;height:32px;font-size:10px">Employer Sign in</a>
</section>

<section class="section signin">
  <div class="band-photo" style="top:0;height:262px" role="img" aria-label="Photo of a smiling professional, darkened"></div>
  <svg class="ribbon" width="1200" height="46" viewBox="0 0 1200 46" aria-hidden="true">
    <rect width="1200" height="16" fill="#e8435a"/>
    <polygon points="0,16 300,16 320,4 880,4 900,16 1200,16 1200,46 0,46" fill="#fff"/>
  </svg>
  <h2 class="abs center title-light signin-title"><span class="accent">Contractor</span> <b>Sign In /</b> <span class="accent">Profile</span></h2>
  <div class="field" style="left:268px;top:67px;width:662px">Your Name</div>
  <div class="field" style="left:268px;top:96px;width:662px">Job Title <svg class="chev" viewBox="0 0 9 6"><path d="M1 1l3.5 3.5L8 1" fill="none" stroke="#fff" stroke-width="1.4"/></svg></div>
  <div class="field" style="left:268px;top:126px;width:662px">Years Experience <svg class="chev" viewBox="0 0 9 6"><path d="M1 1l3.5 3.5L8 1" fill="none" stroke="#fff" stroke-width="1.4"/></svg></div>
  <div class="field" style="left:268px;top:156px;width:662px">Skill Areas <svg class="chev" viewBox="0 0 9 6"><path d="M1 1l3.5 3.5L8 1" fill="none" stroke="#fff" stroke-width="1.4"/></svg></div>
  <div class="field" style="left:268px;top:186px;width:662px">Gender <svg class="chev" viewBox="0 0 9 6"><path d="M1 1l3.5 3.5L8 1" fill="none" stroke="#fff" stroke-width="1.4"/></svg></div>
  <div class="captcha" style="left:269px;top:217px;width:197px;height:30px"><span class="box"></span>I'm not a robot<span class="badge"></span></div>
  <div class="form-btn" style="left:475px;top:217px;width:455px;height:30px">SIGN IN AS A CONTRACTOR</div>
</section>

<section class="section search">
  <div class="stripe-band"></div>
  <h2 class="abs center title search-title"><span class="accent">RivoLink</span> Employer <span class="accent">Search</span></h2>
  <div class="panel-head" style="left:264px;top:95px;width:328px">SEARCH FOR A CONTRACTOR</div>
  <div class="filter" style="top:136px">Contractor Type<span class="value">Geologist</span><svg class="chev" viewBox="0 0 9 6"><path d="M1 1l3.5 3.5L8 1" fill="none" stroke="#333" stroke-width="1.4"/></svg></div>
  <div class="filter" style="top:165px">Country<span class="value">Australia</span><svg class="chev" viewBox="0 0 9 6"><path d="M1 1l3.5 3.5L8 1" fill="none" stroke="#333" stroke-width="1.4"/></svg></div>
  <div class="filter" style="top:194px">Skill 1<span class="value">Sequence Stratigraphy</span><svg class="chev" viewBox="0 0 9 6"><path d="M1 1l3.5 3.5L8 1" fill="none" stroke="#333" stroke-width="1.4"/></svg></div>
  <div class="filter" style="top:223px">Skill 2<span class="value">New Ventures</span><svg class="chev" viewBox="0 0 9 6"><path d="M1 1l3.5 3.5L8 1" fill="none" stroke="#333" stroke-width="1.4"/></svg></div>
  <div class="filter" style="top:252px">Skill 2<span class="value">New Ventures</span><svg class="chev" viewBox="0 0 9 6"><path d="M1 1l3.5 3.5L8 1" fill="none" stroke="#333" stroke-width="1.4"/></svg></div>
  <div class="filter" style="top:281px">Years Experience<span class="value">15-20 yrs</span><svg class="chev" viewBox="0 0 9 6"><path d="M1 1l3.5 3.5L8 1" fill="none" stroke="#333" stroke-width="1.4"/></svg></div>
  <div class="filter" style="top:310px">Gender<span class="value">Male</span><svg class="chev" viewBox="0 0 9 6"><path d="M1 1l3.5 3.5L8 1" fill="none" stroke="#333" stroke-width="1.4"/></svg></div>
  <div class="search-btn">SEARCH CONTRACTOR</div>

  <div class="panel-head" style="left:609px;top:95px;width:328px">SWITCH TO LIST VIEW</div>
  <div class="result-panel">
    <svg width="328" height="254" viewBox="0 0 328 254" aria-hidden="true">
      <g fill="none" stroke="#e8435a" stroke-width="3">
        <circle cx="83" cy="52" r="43" stroke-dasharray="200 70"/>
        <circle cx="247" cy="52" r="43" stroke-dasharray="200 70"/>
        <circle cx="166" cy="124" r="43" stroke-dasharray="200 70"/>
        <circle cx="83" cy="196" r="43" stroke-dasharray="200 70"/>
        <circle cx="247" cy="196" r="43" stroke-dasharray="200 70"/>
      </g>
      <g fill="#c9b3a4" stroke="#fff" stroke-width="2">
        <circle cx="83" cy="52" r="36" role="img" aria-label="Contractor portrait"/>
        <circle cx="247" cy="52" r="36" role="img" aria-label="Contractor portrait"/>
        <circle cx="166" cy="124" r="36" role="img" aria-label="Contractor portrait"/>
        <circle cx="83" cy="196" r="36" role="img" aria-label="Contractor portrait"/>
        <circle cx="247" cy="196" r="36" role="img" aria-label="Contractor portrait"/>
      </g>
    </svg>
  </div>
</section>

<section class="section testimonial">
  <div class="band-photo alt" style="top:0;height:254px" role="img" aria-label="Photo of smiling colleagues, darkened"></div>
  <svg class="ribbon" width="1200" height="40" viewBox="0 0 1200 40" aria-hidden="true">
    <rect width="1200" height="14" fill="#e8435a"/>
    <polygon points="0,14 300,14 320,2 880,2 900,14 1200,14 1200,40 0,40" fill="#fff"/>
  </svg>
  <h2 class="abs center title-light" style="top:4px"><span class="accent">What</span> <b>Clients</b> <span class="accent">Say</span> <b>About</b> Us</h2>
  <p class="abs quote">Praesent semper erat id urlipsnanibus tempor. Suspendisse sodales neque eu erat iuspendisse nec volutpat ante, sitamet dignissim lectus. Praesent eros ex, dumvitae alipsum Isiodudm ntetempus congue.disse nec volutpat antesit amet dignissim lectus lipsumraesent eros ex, dignissim et libero sed, fring</p>
  <div class="abs center quote-mark">”</div>
  <div class="avatar" role="img" aria-label="Client portrait"></div>
  <div class="abs center person">Dana Whitlock</div>
  <div class="abs center role">CEO of Petroleum Firm</div>
  <div class="dots"><span class="on"></span><span></span><span></span></div>
</section>

<section class="section team">
  <h2 class="abs center team-title">RivoLink Team</h2>
  <div class="card" style="left:249px"><div class="card-photo" role="img" aria-label="Team member portrait"></div><div class="card-caption"><div class="card-name">Team Member Name</div><div class="card-role">Marketing Manager</div></div></div>
  <div class="card" style="left:428px"><div class="card-photo" role="img" aria-label="Team member portrait"></div><div class="card-caption"><div class="card-name">Team Member Name</div><div class="card-role">Marketing Manager</div></div></div>
  <div class="card" style="left:609px"><div class="card-photo" role="img" aria-label="Team member portrait"></div><div class="card-caption"><div class="card-name">Team Member Name</div><div class="card-role">Marketing Manager</div></div></div>
  <div class="card" style="left:789px"><div class="card-photo" role="img" aria-label="Team member portrait"></div><div class="card-caption"><div class="card-name">Team Member Name</div><div class="card-role">Marketing Manager</div></div></div>
  <div class="ghost-btn">MEET OUR FULL TEAM</div>
</section>

<section class="section contact">
  <div class="band-photo" style="top:0;height:276px" role="img" aria-label="Photo of people at a meeting, darkened"></div>
  <svg class="ribbon" width="1200" height="40" viewBox="0 0 1200 40" aria-hidden="true">
    <rect width="1200" height="10" fill="#e8435a"/>
    <polygon points="0,10 300,10 320,0 880,0 900,10 1200,10 1200,40 0,40" fill="#fff"/>
  </svg>
  <h2 class="abs center title-light contact-title"><b>Contact</b> <span class="accent">Us</span></h2>
  <div class="field" style="left:271px;top:72px;width:326px;height:24px">Your Full Name</div>
  <div class="field" style="left:608px;top:72px;width:324px;height:24px">Your Last Name</div>
  <div class="field" style="left:271px;top:108px;width:326px;height:24px">Email Address</div>
  <div class="field" style="left:608px;top:108px;width:324px;height:24px">Contact Telephone Number</div>
  <div class="field" style="left:271px;top:145px;width:661px;height:57px;align-items:flex-start;padding-top:5px">Your Message</div>
  <div class="captcha" style="left:271px;top:212px;width:326px;height:26px"><span class="box"></span>I'm not a robot<span class="badge"></span></div>
  <div class="form-btn" style="left:608px;top:212px;width:324px;height:26px">SEND</div>
</section>

<footer class="section footer">
  <div class="abs center footer-brand"><span class="brand-dot"></span>RivoLink</div>
  <div class="abs center footer-info">
    <div>Location: Suite 4.08, Level 4, Harbour House, 12 Quay Lane, Sydney, NSW 2000, Australia</div>
    <div><b>Opening hours:</b> Mon - Fri 9am - 6pm GMT<span class="sep">/</span><b>Telephone:</b> 1300 555 019 (AUS)<span class="sep">/</span><b>Email:</b> info@rivolink.com</div>
  </div>
  <div class="social" aria-label="Social links"><span></span><span></span><span></span><span></span><span></span></div>
  <div class="abs center copyright">© 2017 <b>RivoLink</b>. All Rights Reserved. <span style="color:var(--red);margin:0 8px">/</span> <a>Privacy Policy</a></div>
</footer>

</body>
</html>
```